Classic Personal Business Card in Regatta Dunmore Hale Style (Horizontal - Raised Ink)

If you ever seen a Dunmore Hale Regatta shirt, you will know that the signature of that shirt is small monogrammed icon on the left pocket. I envision my personal business card using some of these elements. I am in the oil exploration industry, which is very conservative and I want a card that looks great but still reflects that classic conservatism. I specifically do land management work, which means I determine who owns mineral rights, I lease those rights for larger companies to then drill for crude oil and natural gas

1. I have designed a small logo (which definitely could use some help) that I would like to be pretty small, centered in the middle of the card, and near the top of the card (color - navy blue or similar) Please feel free to make this logo infinitely better. However, I am not looking for anything abstract/

2. I want my name and designation (Marcus J. Thornbury, RPL) centered in the middle of the card. As far as font, I'm looking for a classic, strong (almost masculine) cursive font (I realize masculine + cursive is a little oxymoronic) and I would like it to the color to be Gold.

3. I would like my name (see above) to sit on top of a thin, centered navy blue (or similar) line as if it were almost a signature on a line. I want the lower-case letters that normally would dip below the line (which is y and p in my case) to do the same. I'll attach an example to help illustrate what I mean.

4. The rest of the card is my contact information. Because I am shoot for a more centered and balance look, I would like the placement of my contact information to also be centered and balance. Font should be a very classic, professional font. My first inclination is to use black for the color but I'm open to other suggestions.

Contact information:

Phone: (XXX) XXX-XXXX
Email: xxxxxxx@mailbox-example.net

Important Note: My hope is to have these printed with Raised Ink on High Quality High Quality Card Stock so it must conform to this Necessity.

Project Deadline Extended Reason: I am having major internet trouble. So I am not able to look at the submissions and provide feedback in a timely fashion. Also, it is difficult to access the site from just my phone. Added Saturday, November 22, 2014

Target Market(s)

US Oil Executives

Industry/Entity Type

Conservative

Contact Information for Business Card

I've posted a new logo that needs some clean up and a new idea for the top and bottom border of the card. I would like the logo to be centered in the top border with a white barrier on either side between the logo and the border. I've also posted color codes below.

Thanks

Requirements
Must have
• Color Codes:
• Blue: R - 0 G - 0 B - 102
• Gold R - 102 G - 102 B - 0

```html
<!DOCTYPE html>
<html lang="en">
<head>
<meta charset="utf-8">
<title>Marcus J. Thornbury, RPL – Business Card</title>
<link rel="stylesheet" href="https://fonts.googleapis.com/css2?family=Shadows+Into+Light+Two&family=Exo+2:wght@400&display=swap">
<style>
  :root {
    --stage: #c9ccd0;
    --card: #121214;
    --card-shade: #1c1c1f;
    --gold: #f2d21a;
    --navy: #2b2f8f;
    --navy-deep: #1e2170;
  }
  html, body {
    margin: 0;
    width: 1200px;
    height: 823px;
    overflow: hidden;
    background: var(--stage);
  }
  .card {
    position: absolute;
    left: 110px;
    top: 131px;
    width: 980px;
    height: 560px;
    background: var(--card);
    box-shadow: 0 10px 30px rgba(0,0,0,.35);
    overflow: hidden;
  }
  .card__facets {
    position: absolute;
    left: 0;
    right: 0;
    bottom: 0;
    height: 230px;
    background: linear-gradient(180deg, rgba(28,28,31,0) 0%, var(--card-shade) 70%, #202024 100%);
  }
  .brand {
    position: absolute;
    top: 58px;
    left: 0;
    right: 0;
    display: flex;
    justify-content: center;
    align-items: center;
    gap: 12px;
  }
  .brand__dot {
    width: 34px;
    height: 34px;
    border: 2px solid var(--navy);
    border-radius: 50%;
    box-sizing: border-box;
  }
  .brand__name {
    font-family: "Exo 2", sans-serif;
    font-size: 22px;
    color: var(--navy);
    letter-spacing: 1px;
  }
  .signature {
    position: absolute;
    left: 0;
    right: 0;
    top: 185px;
    text-align: center;
  }
  .signature__name {
    font-family: "Shadows Into Light Two", cursive;
    font-size: 92px;
    line-height: 1;
    color: var(--gold);
    position: relative;
    z-index: 1;
  }
  .signature__title {
    font-family: "Exo 2", sans-serif;
    font-size: 30px;
    color: var(--gold);
    vertical-align: 14px;
    margin-left: 10px;
    position: relative;
    z-index: 1;
  }
  .signature__line {
    position: absolute;
    left: 70px;
    right: 70px;
    top: 300px;
    height: 2px;
    background: var(--navy);
  }
  .contact {
    position: absolute;
    left: 300px;
    top: 350px;
    margin: 0;
    padding: 0;
    list-style: none;
    font-family: "Exo 2", sans-serif;
    font-size: 31px;
    color: var(--gold);
  }
  .contact__item {
    display: flex;
    align-items: center;
    gap: 16px;
    height: 46px;
  }
  .contact__icon {
    width: 34px;
    height: 30px;
    flex: none;
  }
</style>
</head>
<body>
  <main class="card">
    <div class="card__facets" role="img" aria-label="Subtle dark faceted background shapes"></div>

    <div class="brand">
      <span class="brand__dot"></span>
      <span class="brand__name">M.J. Thornbury</span>
    </div>

    <div class="signature__line"></div>
    <div class="signature">
      <span class="signature__name">Marcus J. Thornbury</span><span class="signature__title">RPL</span>
    </div>

    <ul class="contact">
      <li class="contact__item">
        <svg class="contact__icon" viewBox="0 0 34 30" aria-hidden="true">
          <rect x="1" y="0" width="32" height="30" rx="6" fill="var(--navy)"/>
          <path d="M11 7c2-1 3 0 4 2l1 3c0 1-1 2-2 2 1 3 3 5 6 6 0-1 1-2 2-2l3 1c2 1 3 2 2 4-1 2-3 3-6 2-6-2-10-6-12-12-1-3 0-5 2-6z" fill="var(--card)"/>
        </svg>
        <span>(xxx) xxx-xxxx</span>
      </li>
      <li class="contact__item">
        <svg class="contact__icon" viewBox="0 0 34 30" aria-hidden="true">
          <rect x="2" y="5" width="30" height="21" fill="var(--navy)"/>
          <path d="M2 5 L17 17 L32 5 M2 26 L13 15 M32 26 L21 15" stroke="var(--card)" stroke-width="1.5" fill="none"/>
        </svg>
        <span>xxxxxxx@mailbox-example.net</span>
      </li>
    </ul>
  </main>
</body>
</html>
```